Website Design Project

KEL VISA is looking for a professional designer who would re-design our current website www.bordwellpassage.com.
KEL provides immigration and visa services to the US in these markets: Slovakia, Czech republic and USA. We would like to target Poland and Russia as well.
Who are we: KEL is Dubrik & Helmsley international law firm with offices in New York, Bratislava and Prague. We are licensed in several jurisdiction such as New York, England and Wales, and Slovakia.
Additionally, we are offering online products in our E-shop, such as E-books, E-brochures, DVD's regarding visa and immigration opportunities into United States.
Our targeted audience is: young students who want to study in the US, young professionals looking for employment in the US, investors who want to invest to the US, people looking to get their green card (permanent residency in the US), etc.
Our new design: should look professional, communicate financial safety, professional services, increase sales, but also feel emotional for people who are looking forward to start their new life in the United States.
Updates

Dear Designers, 

we have changed our project from refundable to committed! 

Cant wait to see your designs! 

Thanks! 

KEL VISA 

Designers! 

We have attached pictures od old NY so you may wanna work with them! 

Target Market(s)

USA, Slovakia, Czech Republic

Industry/Entity Type

Financial

Requirements
Nice to have
• 1) pictures of old New York, Tarrow Quay.
2) pictures of the US
Should not have
• KEL VISA is operated by law form Dubrik & Helmsley. We are not looking for boring, old fashioned and profesional website for "legal practitioners". No dark colors, no brown color, no dark green color. it should look light and fresh.

KEL VISA is fresh, new, modern, professional and flexible TEAM of YOUNG and SMART immigration lawyers who want to make a difference. Our website MUST reflect our philosophy. "Success is all about people that we meet and the things we create with them".

```html
<!DOCTYPE html>
<html lang="en">
<head>
<meta charset="utf-8">
<title>KEL Visa and Immigration</title>
<link href="https://fonts.googleapis.com/css2?family=Titillium+Web:wght@400;600;700&family=Arimo:ital,wght@0,400;0,700;1,400;1,700&display=swap" rel="stylesheet">
<style>
:root{
  --blue:#5ba7d6;
  --nav:#6cb3de;
  --orange:#f09a22;
  --orange-text:#f39a1c;
  --text:#333;
  --muted:#555;
  --panel:#f2f2f2;
  --footer:#232323;
  --footer-text:#cfcfcf;
}
*{margin:0;padding:0;box-sizing:border-box}
html,body{width:1059px;height:1200px;overflow:hidden;background:#fff}
.page{width:1200px;height:1360px;position:relative;transform:scale(0.8825);transform-origin:0 0;font-family:"Arimo",Arial,sans-serif;color:var(--text)}
.abs{position:absolute}
.brand{left:110px;top:10px;font-family:"Titillium Web",sans-serif;font-weight:700;font-size:34px;color:var(--blue);letter-spacing:.5px}
.tagline{left:112px;top:50px;font-size:12px;font-style:italic;color:#444;letter-spacing:.3px}
.call{right:110px;top:15px;font-family:"Titillium Web",sans-serif;font-size:15px;color:#444}
.call b{color:var(--blue);font-weight:600;margin-left:4px}
.search{left:874px;top:38px;width:216px;height:25px;border:1px solid #bbb;border-radius:13px;font-size:11px;font-style:italic;color:#999;padding:5px 14px}
.search svg{position:absolute;right:10px;top:5px}
.nav{left:0;top:78px;width:1200px;height:43px;background:var(--nav);display:flex;padding-left:110px;align-items:center}
.nav span{color:#fff;font-family:"Titillium Web",sans-serif;font-size:13px;padding:0 16px;border-left:1px solid rgba(255,255,255,.45);line-height:18px}
.nav span:first-child{padding-left:0;border-left:0}
.hero{left:0;top:121px;width:1200px;height:339px;background:linear-gradient(180deg,#cfcfcf 0%,#b5b5b5 50%,#4a4a4a 82%,#2b2b2b 100%)}
.quote{left:412px;top:146px;width:690px;font-family:"Titillium Web",sans-serif;font-size:35px;line-height:37px;color:#fff}
.quote b{font-weight:700}
.btn-hero{left:982px;top:222px;width:108px;height:37px;background:linear-gradient(#f6ac3a,#ec8f16);border-radius:3px;color:#fff;font-family:"Titillium Web",sans-serif;font-size:16px;text-align:center;line-height:37px}
.dots{left:1028px;top:441px;display:flex;gap:6px}
.dots i{width:11px;height:11px;border-radius:50%;background:#fff;display:block}
.dots i:first-child{background:var(--blue)}
.welcome{left:110px;top:489px;font-family:"Titillium Web",sans-serif;font-weight:600;font-size:22px;color:var(--blue);letter-spacing:.8px}
.rule{left:110px;top:521px;width:980px;height:1px;background:#ddd}
.photo{background:linear-gradient(135deg,#2c5f9e,#6c9fcf 60%,#3b6fae)}
.intro-title{left:301px;top:539px;font-family:"Titillium Web",sans-serif;font-size:19px;color:#333}
.intro-text{left:301px;top:567px;width:790px;font-size:12px;line-height:18px;letter-spacing:.4px;color:#333}
.btn-more{left:1000px;top:622px;width:90px;height:26px;background:#74b6e0;border-radius:3px;color:#fff;font-size:12px;text-align:center;line-height:26px;letter-spacing:.4px}
.panel{background:var(--panel)}
.panel h3{font-family:"Titillium Web",sans-serif;font-weight:400;font-size:18px;color:var(--blue);padding:14px 9px 5px;border-bottom:1px solid #d6d6d6}
.links{list-style:none;padding:8px 9px 0 10px}
.links li{display:flex;justify-content:space-between;font-size:12px;letter-spacing:.4px;padding:8px 0 6px;border-bottom:1px dotted #888}
.links li small{font-size:10px}
.links li:last-child{border-bottom:0}
.product{display:flex;gap:10px;margin:14px 10px 0;padding-bottom:13px;border-bottom:1px dotted #888}
.product:last-child{border-bottom:0}
.product .thumb{width:75px;height:55px;flex:none;border:1px solid #ccc}
.product h4{font-family:"Titillium Web",sans-serif;font-weight:400;font-size:15px;color:#333;line-height:18px}
.product p{font-size:12px;line-height:15px;letter-spacing:.5px;color:#444}
.service{left:410px;width:380px;height:110px;border-bottom:1px dotted #777;display:flex;gap:30px}
.service .thumb{width:70px;height:66px;flex:none}
.service h4{font-family:"Titillium Web",sans-serif;font-weight:400;font-size:19px;color:var(--blue);line-height:22px}
.service p{font-size:12px;line-height:18px;letter-spacing:.4px;margin-top:6px}
.orange{color:var(--orange-text)}
.post{margin:0 10px;padding:15px 0 10px;border-bottom:1px dotted #888}
.post:last-child{border-bottom:0}
.post em{font-size:11px;color:#444;display:block}
.post p{font-size:12px;line-height:14px;letter-spacing:.5px;text-align:justify}
.post a{display:block;text-align:right;font-size:12px;font-style:italic;color:var(--orange-text);margin-top:10px;text-decoration:none}
.footer{left:0;top:1168px;width:1200px;height:192px;background:var(--footer);border-top:6px solid #555}
.fcol{top:1185px;color:var(--footer-text);font-size:11px;line-height:18px;letter-spacing:.8px}
.fcol h5{font-size:14px;color:#fff;font-weight:700;letter-spacing:0;padding-bottom:4px;border-bottom:1px dotted #888;margin-bottom:10px}
.fcol ul{list-style:none}
.fcol li::before{content:"\25AA";margin-right:5px}
.social{display:flex;gap:12px;margin-top:4px}
.social i{width:33px;height:33px;border-radius:50%;background:#444;display:block}
.testimonial{font-style:italic;font-size:12px;line-height:18px;color:#e6e6e6;padding-left:19px;text-align:justify;position:relative}
.qmark{font-family:Georgia,serif;font-size:28px;color:#ddd;position:absolute;font-style:normal;font-weight:700}
.copy{left:0;top:1336px;width:1200px;text-align:center;font-size:12px;color:#999;letter-spacing:1px}
</style>
</head>
<body>
<div class="page">
  <div class="abs brand">KEL Visa and Immigration</div>
  <div class="abs tagline">Dubrik &amp; Helmsley Immigration Attorneys, US Visa, US Green Card, ESTA</div>
  <div class="abs call">Call us today on <b>(212) 555-0147</b></div>
  <div class="abs search">Search something...
    <svg width="14" height="14" viewBox="0 0 14 14"><circle cx="6" cy="6" r="4" fill="none" stroke="#aaa" stroke-width="1.6"/><line x1="9" y1="9" x2="13" y2="13" stroke="#aaa" stroke-width="1.8"/></svg>
  </div>

  <nav class="abs nav">
    <span>Consultation</span><span>Visitors Visas</span><span>Work Visas</span><span>Business Visas</span><span>Family Visas</span><span>Student Visas</span><span>Green Card</span><span>Visa Forms</span><span>KEL E-shop</span><span>Visa News</span>
  </nav>

  <div class="abs hero" role="img" aria-label="Black and white night skyline of New York across the water"></div>
  <div class="abs quote">"<b>Success</b> is all about people that we meet and the things we create with them "</div>
  <div class="abs btn-hero">Read more</div>
  <div class="abs dots"><i></i><i></i><i></i><i></i></div>

  <h2 class="abs welcome">WELCOME TO KEL VISA AND IMMIGRATION</h2>
  <div class="abs rule"></div>
  <div class="abs photo" style="left:110px;top:541px;width:162px;height:108px" role="img" aria-label="Statue of Liberty against a blue sky"></div>
  <div class="abs intro-title">Visas to the U.S. and U.S. Immigration</div>
  <p class="abs intro-text">Lorem Ipsum is simply dummy text of the printing and typesetting industry. Lorem Ipsum has been the industry's standard dummy text ever since the 1500s, when an unknown printer took a galley of type and scrambled it to make a type specimen book. It has survived not only five centuries, but also the leap into electronic typesetting, remaining</p>
  <div class="abs btn-more">› Read more</div>

  <section class="abs panel" style="left:110px;top:695px;width:242px;height:201px">
    <h3>Important Links</h3>
    <ul class="links">
      <li>Visa Forms Download<small>Free</small></li>
      <li>Business Visa for 6 Months<small>$400</small></li>
      <li>Tourist Visa for 6 Months<small>$300</small></li>
      <li>ESTA Registration<small>$50</small></li>
      <li>Consultation<small>$65</small></li>
    </ul>
  </section>

  <section class="abs panel" style="left:110px;top:916px;width:242px;height:213px">
    <h3>KEL E-Products</h3>
    <div class="product">
      <div class="thumb" style="background:linear-gradient(135deg,#e9e9f2,#b9a6e0 50%,#f0c9e6)" role="img" aria-label="Stack of colourful DVD discs"></div>
      <div><h4>Visa &nbsp;DVD</h4><p>Lorem ipsum dolor jit amet,consectetuer</p></div>
    </div>
    <div class="product">
      <div class="thumb" style="background:linear-gradient(#fafafa,#e0e0e0)" role="img" aria-label="Printed visa application form"></div>
      <div><h4>Visa Forms</h4><p>Lorem ipsum dolor sit amet,consectetuer</p></div>
    </div>
  </section>

  <div class="abs service" style="top:705px">
    <div class="thumb photo" style="background:linear-gradient(135deg,#c9a88a,#f2e7dc)" role="img" aria-label="Smiling family of four"></div>
    <div><h4>Family Visa</h4><p>Lorem Ipsum is simply dummy text of the printing and type industry...[ <span class="orange">more</span> ]</p></div>
  </div>
  <div class="abs service" style="top:815px">
    <div class="thumb" style="background:linear-gradient(135deg,#cfe2f0,#f5f5f5 55%,#3c4a6a)" role="img" aria-label="Young businessman in a suit"></div>
    <div><h4>Work Visa</h4><p>Lorem Ipsum is simply dummy text of the printing and type industry...[ <span class="orange">more</span> ]</p></div>
  </div>
  <div class="abs service" style="top:925px">
    <div class="thumb" style="background:linear-gradient(135deg,#5d6570,#dfe5ea 50%,#f4f4f4)" role="img" aria-label="Business people meeting at a desk"></div>
    <div><h4>Business Visa</h4><p>Lorem Ipsum is simply dummy text of the printing and type industry...[ <span class="orange">more</span> ]</p></div>
  </div>
  <div class="abs service" style="top:1035px;border-bottom:0">
    <div class="thumb" style="background:linear-gradient(135deg,#a7c27a,#eef2e2 50%,#6c8f4c)" role="img" aria-label="Student with books outdoors"></div>
    <div><h4>Study Visa</h4><p>Lorem Ipsum is simply dummy text of the printing and type industry...[ <span class="orange">more</span> ]</p></div>
  </div>

  <section class="abs panel" style="left:848px;top:693px;width:242px;height:436px">
    <h3>Recent Posts</h3>
    <div class="post"><em>Posted on Dec 1st, 2012</em><p>Lorem Ipsum is simply dummy text the lokknyi nyment printing.</p><a>› Read more</a></div>
    <div class="post"><em>Posted on Nov 7th, 2012</em><p>Lorem Ipsum is simply dummy text the lokknyi nyment printing.</p><a>› Read more</a></div>
    <div class="post"><em>Posted on October 10th, 2012</em><p>Lorem Ipsum is simply dummy text the lokknyi nyment printing.</p><a>› Read more</a></div>
    <div class="post"><em>Posted on October 5th, 2012</em><p>Lorem Ipsum is simply dummy text the lokknyi nyment printing.</p><a>› Read more</a></div>
  </section>

  <footer class="abs footer"></footer>
  <div class="abs fcol" style="left:110px;width:178px">
    <h5>Links</h5>
    <ul>
      <li>Partner Pages</li>
      <li>Dubrik &amp; Helmsley</li>
      <li>+421 Foundation</li>
      <li>Incorporate Company LLC Ltd.<br>&nbsp;&nbsp;in USA England Hong Kong or<br>&nbsp;&nbsp;Offshore</li>
    </ul>
  </div>
  <div class="abs fcol" style="left:357px;width:126px">
    <h5>Contact Us</h5>
    Dubrik &amp; Helmsley<br>New York<br>48 W 71st Street #4B<br>New York 10023 NY<br><span class="orange">+1 (212) 555-0147</span>
  </div>
  <div class="abs fcol" style="left:556px;width:123px">
    <h5>Get Connected</h5>
    <div class="social"><i></i><i></i><i></i></div>
  </div>
  <div class="abs fcol" style="left:756px;width:334px">
    <h5>Testimonial</h5>
    <div class="testimonial">
      <span class="qmark" style="left:0;top:-6px">“</span>
      Praesent uluoles tie lacus. Aenean non ummyen drerit maurisus porta. Fuse suscip iquam erat volut patis ais. Integer lacibul libro nisl porta.
      <span class="qmark" style="right:0;bottom:-24px">”</span>
    </div>
    <div style="text-align:right;margin-top:20px;font-style:italic;font-size:12px;color:#999">- Mr. Peter Adler</div>
  </div>
  <div class="abs copy">© 2012 KEL Visa and Immigration. All Rights Reserved</div>
</div>
</body>
</html>
```